Promotion Layer (UI Design)

What we need is not a classical App Design.
We need a UI Design for a SDK, which appears as Layer in different apps.
The layer will contain a list/library which will show cool goodies for the app user.

The attached file will give you all the details you need to start.

Note: The Screenshots do show app content. But these are just place holders.
The content is NOT part of the design task. Because we just provide the layer...

The crucial part of this task is, to create a UI design, that is stylish, simple and does not harm the 3rd party app, where it will be showed. While you design it, allways try to think "do I like this, when it appears in my own app"

Your files should be made in the right size/dimensions of ios.

Industry/Entity Type

Library

Font styles to use
Sans Serif

Requirements
Must have
• Must fit the iOS 7 Style

```html
<!DOCTYPE html>
<html lang="en">
<head>
<meta charset="utf-8">
<title>Bag Outlet – Discover Layer</title>
<link rel="stylesheet" href="https://fonts.googleapis.com/css2?family=Open+Sans:wght@300;400;600;700&display=swap">
<style>
  :root {
    --page-bg: #e4e4e4;
    --blue: #2f86c8;
    --blue-dark: #1f6fae;
    --white: #ffffff;
    --ink: #3a3a3a;
    --ink-soft: #6f6f6f;
    --ink-faint: #9a9a9a;
    --accent-red: #e0474c;
    --row-bg: #efefef;
    --row-line: #dcdcdc;
    --card-bg: #f3f3f3;
    --photo-a: #8d8f94;
    --photo-b: #d9d8d4;
    --map-a: #e9e5dc;
    --map-b: #cfe0ee;
  }
  * { box-sizing: border-box; margin: 0; padding: 0; }
  html, body {
    width: 1110px; height: 1200px; overflow: hidden;
    background: var(--page-bg);
    font-family: "Open Sans", Arial, sans-serif;
    color: var(--ink);
  }
  .screen {
    position: absolute; left: 235px; top: 32px;
    width: 640px; height: 1136px;
    background: var(--white);
    overflow: hidden;
    box-shadow: 0 4px 30px rgba(0,0,0,.12);
    display: flex; flex-direction: column;
  }
  .top-bar { background: var(--blue); color: var(--white); height: 128px; }
  .status-bar {
    height: 40px; display: flex; align-items: center; justify-content: space-between;
    padding: 0 14px; font-size: 22px; font-weight: 600;
  }
  .carrier { display: flex; align-items: center; gap: 6px; }
  .nav-bar {
    height: 88px; display: flex; align-items: center; justify-content: space-between;
    padding: 0 26px 0 30px;
  }
  .nav-title { font-size: 38px; font-weight: 700; letter-spacing: .3px; }
  .nav-actions { display: flex; gap: 34px; align-items: center; }
  .sub-bar {
    height: 88px; display: flex; align-items: center; justify-content: space-between;
    padding: 0 24px; border-bottom: 1px solid #ececec;
  }
  .sub-title { font-size: 30px; font-weight: 300; color: var(--ink-soft); }
  .circle-btn {
    width: 48px; height: 48px; border-radius: 50%; border: 2px solid #9d9d9d;
    display: flex; align-items: center; justify-content: center;
    color: #7d7d7d; font-size: 24px;
  }
  .media-card {
    margin: 16px 20px 0; padding: 14px; background: var(--card-bg);
    display: flex; height: 430px;
  }
  .store-photo { flex: 1; background: linear-gradient(160deg, var(--photo-b), var(--photo-a)); }
  .store-map { flex: 1; background: linear-gradient(120deg, var(--map-a) 55%, var(--map-b)); }
  .details { padding: 44px 48px 0; flex: 1; }
  .store-name { font-size: 40px; font-weight: 300; color: var(--ink); }
  .store-meta {
    margin-top: 10px; color: var(--accent-red); display: flex; gap: 22px; align-items: baseline;
  }
  .store-meta .place { font-size: 26px; font-weight: 600; }
  .store-meta .phone { font-size: 17px; }
  .hours { margin-top: 8px; font-size: 16px; color: var(--accent-red); text-transform: uppercase; }
  .hours span { text-transform: none; }
  .about { margin-top: 36px; font-size: 17px; line-height: 1.45; color: var(--ink-soft); }
  .about p + p { margin-top: 12px; }
  .action-list { list-style: none; background: var(--row-bg); }
  .action-row {
    height: 88px; display: flex; align-items: center; justify-content: space-between;
    padding: 0 30px 0 48px; border-top: 2px solid var(--row-line);
    font-size: 28px; font-weight: 300; color: var(--ink-soft);
  }
</style>
</head>
<body>
  <main class="screen">
    <header class="top-bar">
      <div class="status-bar">
        <div class="carrier">
          <svg width="30" height="20" viewBox="0 0 30 20" aria-hidden="true">
            <rect x="0" y="15" width="4" height="5" fill="#fff"/>
            <rect x="6" y="11" width="4" height="9" fill="#fff"/>
            <rect x="12" y="7" width="4" height="13" fill="#fff"/>
            <rect x="18" y="3" width="4" height="17" fill="#fff"/>
          </svg>
          CARRIER
        </div>
        <svg width="20" height="24" viewBox="0 0 20 24" aria-hidden="true">
          <path d="M5 11V7a5 5 0 0 1 10 0v4" fill="none" stroke="#fff" stroke-width="2.5"/>
          <rect x="2" y="11" width="16" height="12" rx="2" fill="#fff"/>
        </svg>
        <svg width="50" height="22" viewBox="0 0 50 22" aria-hidden="true">
          <rect x="1" y="1" width="42" height="20" rx="3" fill="none" stroke="#fff" stroke-width="2"/>
          <rect x="4" y="4" width="36" height="14" fill="#fff"/>
          <rect x="44" y="7" width="4" height="8" fill="#fff"/>
        </svg>
      </div>
      <div class="nav-bar">
        <h1 class="nav-title">Discover</h1>
        <div class="nav-actions">
          <svg width="44" height="44" viewBox="0 0 44 44" aria-label="Search">
            <circle cx="18" cy="18" r="14" fill="none" stroke="#fff" stroke-width="3"/>
            <line x1="28" y1="28" x2="42" y2="42" stroke="#fff" stroke-width="3"/>
          </svg>
          <svg width="44" height="44" viewBox="0 0 44 44" aria-label="Compose">
            <path d="M26 4H4v36h36V18" fill="none" stroke="#fff" stroke-width="3"/>
            <path d="M16 28l4-10L36 2l6 6-16 16z" fill="none" stroke="#fff" stroke-width="3"/>
          </svg>
        </div>
      </div>
    </header>

    <nav class="sub-bar">
      <div class="circle-btn" aria-label="Back">
        <svg width="24" height="20" viewBox="0 0 24 20"><path d="M22 10H3M10 2L2 10l8 8" fill="none" stroke="#7d7d7d" stroke-width="2"/></svg>
      </div>
      <h2 class="sub-title">Bag Outlet</h2>
      <div class="circle-btn" aria-label="Offers">%</div>
    </nav>

    <section class="media-card">
      <div class="store-photo" role="img" aria-label="Store interior with suits and jackets on display rails"></div>
      <div class="store-map" role="img" aria-label="Street map showing the store location beside a lake"></div>
    </section>

    <section class="details">
      <h3 class="store-name">Bag Outlet</h3>
      <div class="store-meta">
        <span class="place">Halden Moss, Alder Bay, CA &nbsp;Ridgeview Mall</span>
        <span class="phone">Phone : 104418 - 20761</span>
      </div>
      <p class="hours">Opening times <span>Mon-Sat 10:00 - 19:00</span></p>
      <div class="about">
        <p>Lorem ipsum dolor sit amet, an mei timeam reformidans, soleat maiestatis in vix, ex justo graeci ciscere cum.</p>
        <p>Qui propriae scaevola expetenda ut, ne habeo tacimates efficiendi sea, id euismod ferent legendos vel. Usu probo tacimates eu. At modus doctus torquatos vix, cibo eligendi liberavisse ad mel.</p>
      </div>
    </section>

    <ul class="action-list">
      <li class="action-row">Call us now : 5047 - 10822
        <span class="circle-btn"><svg width="22" height="22" viewBox="0 0 22 22"><path d="M5 2l4 4-2 3c1 3 3 5 6 6l3-2 4 4-3 4C9 20 2 13 1 5z" fill="none" stroke="#7d7d7d" stroke-width="1.8"/></svg></span>
      </li>
      <li class="action-row">More info
        <span class="circle-btn"><svg width="24" height="20" viewBox="0 0 24 20"><path d="M2 10h19M14 2l8 8-8 8" fill="none" stroke="#7d7d7d" stroke-width="2"/></svg></span>
      </li>
      <li class="action-row">Contact form
        <span class="circle-btn"><svg width="24" height="20" viewBox="0 0 24 20"><path d="M2 10h19M14 2l8 8-8 8" fill="none" stroke="#7d7d7d" stroke-width="2"/></svg></span>
      </li>
    </ul>
  </main>
</body>
</html>
```